Fitness Facility needs a Flyer!

We need a flyer that highlights our 3 different fitness programs.
During the sales process, we'd like to have a visual reference for new prospective clients that highlights our 3 different fitness programs.
The flyer should be colorful, Focus on the different fitness programs BUT! We'd like to steer people towards our middle program, so I'd like the middle program "The Complete Sleek & Sculpted Makeover" to be possibly a little larger than the two others so that the eye naturally gravitates towards that one.
I'd like the flyer to be in a Landscape layout,
Include our logo
Include a group photo of our team
Include the text "Most Popular" over the middle program
Include the text "Save More - 10% discount if paid in full" at the very bottom of the page
I have attached the text of our programs, a group photo, our logo and an example of our last program ... just as an example and not to be duplicated.

```html
<!DOCTYPE html>
<html lang="en">
<head>
<meta charset="utf-8">
<title>PulseForge Programs Flyer</title>
<link rel="stylesheet" href="https://fonts.googleapis.com/css2?family=Anton&family=Oswald:wght@400;500;700&family=Permanent+Marker&display=swap">
<style>
  :root{
    --page:#d8d8d8;
    --asphalt:#4b4b4d;
    --asphalt-dark:#3a3a3c;
    --blue:#4a87cb;
    --yellow:#fde216;
    --ink:#0d0d0d;
    --white:#ffffff;
    --magenta:#e0318f;
    --purple:#6a2fa0;
    --violet:#4b2c8e;
    --sky:#2fa6e0;
  }
  *{box-sizing:border-box;margin:0;padding:0}
  html,body{width:800px;height:1200px;overflow:hidden}
  body{background:var(--page);font-family:"Oswald",sans-serif;color:var(--ink)}

  .flyer{position:absolute;left:20px;top:307px;width:760px;height:585px;overflow:hidden;
    background:radial-gradient(ellipse at 50% 55%,var(--asphalt) 0%,var(--asphalt-dark) 100%);
    box-shadow:0 6px 18px rgba(0,0,0,.25)}

  .brand-band{position:absolute;left:0;top:0;width:760px;height:250px}
  .team-photo{position:absolute;left:240px;top:0;width:520px;height:232px;
    clip-path:polygon(0 0,100% 0,100% 100%,28% 96%,0 88%);
    background:linear-gradient(135deg,#2d5c8a 0%,#5a4a6e 40%,#3b3f55 70%,#7a3d9a 100%)}
  .brand-name{position:absolute;left:36px;top:86px;font-family:"Oswald",sans-serif;font-weight:700;
    font-size:58px;line-height:1;color:var(--white);letter-spacing:-1px}

  .plan{position:absolute}
  .plan-lean{left:34px;top:237px;width:167px;height:230px;background:var(--blue)}
  .plan-blitz{left:522px;top:244px;width:206px;height:206px;background:var(--blue)}
  .plan-featured{left:231px;top:212px;width:257px;height:340px;background:var(--yellow)}

  .plan-title{font-family:"Anton",sans-serif;color:var(--yellow);text-align:center;line-height:.95}
  .plan-lean .plan-title{font-size:38px;margin-top:10px}
  .plan-blitz .plan-title{font-size:40px}
  .plan-tag{display:table;margin:0 auto;background:var(--ink);color:var(--yellow);
    font-family:"Oswald",sans-serif;font-weight:500;text-transform:uppercase;line-height:1.15}
  .plan-lean .plan-tag{font-size:17px;padding:0 4px}
  .plan-blitz .plan-tag{font-size:13px;padding:0 4px;margin-top:12px;margin-bottom:2px}

  .popular-badge{position:absolute;left:280px;top:200px;width:166px;height:26px;border-radius:14px;
    background:var(--ink);color:var(--yellow);font-family:"Permanent Marker",cursive;font-size:17px;
    text-align:center;line-height:27px;z-index:2}
  .featured-title{font-family:"Anton",sans-serif;font-size:37px;line-height:1;text-align:center;margin-top:20px;color:var(--ink)}
  .featured-sub{display:table;margin:2px auto 0;background:var(--ink);color:var(--white);
    font-family:"Oswald",sans-serif;font-weight:500;font-size:14.5px;padding:0 4px;text-transform:uppercase;line-height:1.3}

  .features{list-style:none}
  .features li{display:flex;align-items:flex-start;gap:4px;line-height:1.25;margin-bottom:3px}
  .features svg{flex:0 0 auto;margin-top:1px}
  .features span{background:var(--white);padding:0 2px;-webkit-box-decoration-break:clone;box-decoration-break:clone}
  .features b{font-weight:700}
  .plan-lean .features{margin:26px 8px 0 14px;font-size:8.3px}
  .plan-lean .features svg{width:10px;height:10px}
  .plan-blitz .features{margin:10px 8px 0 12px;font-size:8.1px}
  .plan-blitz .features li{margin-bottom:2.5px}
  .plan-blitz .features svg{width:10px;height:10px}
  .plan-featured .features{margin:18px 22px 0 16px;font-size:9.3px}
  .plan-featured .features svg{width:11px;height:11px}

  .price{position:absolute;border-radius:50%;background:var(--ink);color:var(--white);text-align:center;z-index:3}
  .price-amount{display:block;font-family:"Permanent Marker",cursive;line-height:1}
  .price-unit{display:block;font-size:10px;line-height:1}
  .price-lean{left:139px;top:430px;width:74px;height:74px;padding-top:14px}
  .price-lean .price-amount{font-size:30px}
  .price-featured{left:431px;top:470px;width:78px;height:78px;padding-top:6px}
  .price-featured .price-amount{font-size:30px}
  .price-only{display:block;font-size:9px;line-height:1.1}
  .price-blitz{left:671px;top:445px;width:74px;height:74px;padding-top:14px}
  .price-blitz .price-amount{font-size:28px}

  .dumbbell{position:absolute;left:8px;top:470px;width:110px;height:120px;border-radius:18px;
    background:linear-gradient(160deg,#2b2b2b,#141414);transform:rotate(-18deg)}

  .save-band{position:absolute;left:0;bottom:0;width:760px;height:40px}
  .save-text{position:absolute;left:0;right:0;bottom:6px;text-align:center;color:var(--yellow);
    font-family:"Oswald",sans-serif;font-size:12px;text-transform:uppercase;letter-spacing:.2px}
  .save-text em{font-style:normal;font-family:"Permanent Marker",cursive;font-size:15px}
  .save-text small{font-size:11px;text-transform:none;text-decoration:underline}
</style>
</head>
<body>
<svg width="0" height="0" style="position:absolute" aria-hidden="true">
  <symbol id="tick" viewBox="0 0 12 12">
    <circle cx="6" cy="6" r="6" fill="#0d0d0d"/>
    <path d="M3.2 6.2 5.2 8.1 8.9 3.9" fill="none" stroke="#fff" stroke-width="1.6" stroke-linecap="round" stroke-linejoin="round"/>
  </symbol>
</svg>

<main class="flyer">
  <svg class="brand-band" viewBox="0 0 760 250" aria-hidden="true">
    <defs>
      <linearGradient id="stripeGrad" x1="0" y1="0" x2="1" y2="0">
        <stop offset="0" stop-color="#e0318f"/>
        <stop offset=".6" stop-color="#8a2fa5"/>
        <stop offset="1" stop-color="#4b2c8e"/>
      </linearGradient>
      <linearGradient id="skyGrad" x1="0" y1="0" x2="1" y2="0">
        <stop offset="0" stop-color="#6a2fa0"/>
        <stop offset="1" stop-color="#2fa6e0"/>
      </linearGradient>
    </defs>
    <polygon points="0,0 330,0 300,18 0,22" fill="url(#skyGrad)"/>
    <polygon points="0,26 300,22 250,60 0,62" fill="url(#stripeGrad)"/>
    <polygon points="0,66 280,64 230,100 0,104" fill="#6a2fa0"/>
    <polygon points="0,108 300,106 260,150 0,154" fill="url(#stripeGrad)"/>
    <polygon points="0,158 360,156 330,190 0,196" fill="#e0318f"/>
    <polygon points="60,196 330,190 300,205 60,208" fill="#4b2c8e"/>
  </svg>

  <div class="team-photo" role="img" aria-label="Group photo of the gym members and coaches cheering together"></div>
  <div class="brand-name">PulseForge</div>

  <section class="plan plan-lean">
    <h2 class="plan-title">LEAN</h2>
    <div class="plan-tag">Body Prep</div>
    <ul class="features">
      <li><svg><use href="#tick"/></svg><span>4 Group Training Sessions per week</span></li>
      <li><svg><use href="#tick"/></svg><span><b>Customized</b> Meal Plan</span></li>
      <li><svg><use href="#tick"/></svg><span><b>Monthly</b> BodyComp Scans</span></li>
      <li><svg><use href="#tick"/></svg><span>Supplement List</span></li>
      <li><svg><use href="#tick"/></svg><span>Access to Private PulseForge HuddleHub Group</span></li>
    </ul>
  </section>

  <div class="popular-badge">Most Popular</div>
  <section class="plan plan-featured">
    <h1 class="featured-title">THE COMPLETE</h1>
    <div class="featured-sub">Sleek &amp; Sculpted Makeover</div>
    <ul class="features">
      <li><svg><use href="#tick"/></svg><span><b>UNLIMITED</b> Group Training Sessions Designed to Sculpt &amp; Tone the Body</span></li>
      <li><svg><use href="#tick"/></svg><span><b>Customized AND Phased</b> Nutrition Plans so your metabolism never plateaus</span></li>
      <li><svg><use href="#tick"/></svg><span>Your own <b>Accountability Coach</b> who will be your biggest cheerleader and motivator</span></li>
      <li><svg><use href="#tick"/></svg><span><b>Weekly</b> accountability Check In's</span></li>
      <li><svg><use href="#tick"/></svg><span><b>Bi-weekly</b> 1-on-1 accountability &amp; strategy meetups</span></li>
      <li><svg><use href="#tick"/></svg><span><b>Bi-weekly</b> BodyComp Scans</span></li>
      <li><svg><use href="#tick"/></svg><span>Supplement List to accelerate metabolism</span></li>
      <li><svg><use href="#tick"/></svg><span><b>Exclusive access</b> to PulseForge's Private HuddleHub Page for additional Recipes, Support and Guidance</span></li>
    </ul>
  </section>

  <section class="plan plan-blitz">
    <div class="plan-tag">1-on-1 Fitness</div>
    <h2 class="plan-title">BLITZ</h2>
    <ul class="features">
      <li><svg><use href="#tick"/></svg><span><b>(8) 1-on-1</b> Personal Training Sessions per month</span></li>
      <li><svg><use href="#tick"/></svg><span><b>UNLIMITED</b> Group Training Sessions</span></li>
      <li><svg><use href="#tick"/></svg><span>Customized AND Phased Nutrition Plans</span></li>
      <li><svg><use href="#tick"/></svg><span>Designated Accountability Coach</span></li>
      <li><svg><use href="#tick"/></svg><span>Weekly accountability check in's</span></li>
      <li><svg><use href="#tick"/></svg><span>Weekly BodyComp Scans</span></li>
      <li><svg><use href="#tick"/></svg><span><b>Exclusive</b> Supplement Discounts</span></li>
      <li><svg><use href="#tick"/></svg><span><b>Exclusive</b> access to PulseForge's HuddleHub Page</span></li>
    </ul>
  </section>

  <div class="price price-lean"><span class="price-amount">$47</span><span class="price-unit">per week</span></div>
  <div class="price price-featured"><span class="price-only">ONLY</span><span class="price-amount">$69</span><span class="price-unit">per week</span></div>
  <div class="price price-blitz"><span class="price-amount">$125</span><span class="price-unit">per week</span></div>

  <div class="dumbbell" role="img" aria-label="Black hex dumbbell resting on the gym floor"></div>

  <svg class="save-band" viewBox="0 0 760 40" aria-hidden="true">
    <defs>
      <linearGradient id="saveGrad" x1="0" y1="0" x2="1" y2="0">
        <stop offset="0" stop-color="#e0318f"/>
        <stop offset=".5" stop-color="#8a2fa5"/>
        <stop offset="1" stop-color="#4b2c8e"/>
      </linearGradient>
    </defs>
    <polygon points="180,40 260,14 560,8 640,20 760,18 760,40" fill="url(#saveGrad)"/>
  </svg>
  <p class="save-text">Save More - <em>10%</em> <small>Discount if paid in full</small></p>
</main>
</body>
</html>
```